Kentucky residential recovery center needs a flyer design

We need a flyer design for a 16 bed male residential/inpatient recovery center based in Richmond, Kentucky. The facility provides short term (average 30 day) treatment to those struggling with substace abuse and addiction. The design should communicate trust, assurance, safety.
Our wesite provides more information https://morvalcare.org/treatment-services/residential-treatment/

Target Market(s)

Men (typically 30-50) struggling with substance addiction

```html
<!DOCTYPE html>
<html lang="en">
<head>
<meta charset="utf-8">
<title>Morval Care – Residential/Inpatient Recovery Center Flyer</title>
<link href="https://fonts.googleapis.com/css2?family=Oswald:wght@300;400;500;600&display=swap" rel="stylesheet">
<style>
  :root {
    --backdrop: #5a6068;
    --navy: #22307a;
    --blue: #1f4f8a;
    --green: #12a04c;
    --white: #ffffff;
    --wood-light: #9a8068;
    --wood-dark: #5e4a3a;
    --wall: #cbbfae;
    --ink: #1a1f3a;
  }
  * { box-sizing: border-box; margin: 0; padding: 0; }
  html, body {
    width: 1200px; height: 1200px; overflow: hidden;
    background: var(--backdrop);
    font-family: "Oswald", "Arial Narrow", sans-serif;
  }
  .flyer {
    position: absolute; left: 220px; top: 61px;
    width: 760px; height: 1078px;
    background: var(--white);
    overflow: hidden;
  }
  .hero-lounge {
    position: absolute; left: 0; top: 0; width: 455px; height: 445px;
    background: linear-gradient(100deg, #1f2a66 0%, #1d4a5a 45%, #15804a 100%);
  }
  .hero-lounge::after {
    content: ""; position: absolute; inset: 0;
    background: radial-gradient(ellipse at 45% 70%, rgba(10,40,40,.0) 0%, rgba(5,15,30,.45) 100%);
  }
  .hero-bedroom {
    position: absolute; left: 455px; top: 0; width: 305px; height: 445px;
    background: linear-gradient(180deg, #6b6a74 0%, #8c7358 40%, var(--wood-light) 70%, #7d6552 100%);
  }
  .hero-title {
    position: absolute; left: 60px; top: 255px; z-index: 2;
    color: var(--white); font-weight: 500; font-size: 35px; line-height: 1.15;
    letter-spacing: .2px; text-transform: uppercase;
  }
  .brand-badge {
    position: absolute; left: 548px; top: 52px; width: 148px; height: 148px;
    border-radius: 50%; background: var(--white);
    display: flex; align-items: center; justify-content: center;
  }
  .brand-name {
    color: var(--navy); font-weight: 600; font-size: 20px; letter-spacing: 1px;
    text-transform: uppercase;
  }
  .info-panel {
    position: absolute; left: 0; top: 445px; width: 455px; height: 633px;
    background: linear-gradient(90deg, var(--navy) 0%, #1d5a7a 55%, var(--green) 100%);
    color: var(--white);
  }
  .section-heading {
    position: absolute; left: 60px; top: 43px;
    font-weight: 500; font-size: 34px; line-height: 1.13; text-transform: uppercase;
  }
  .treatment-list { position: absolute; left: 60px; top: 153px; display: flex; gap: 18px; list-style: none; }
  .treatment-item {
    width: 73px; height: 73px; background: var(--white); border-radius: 4px;
    display: flex; flex-direction: column; align-items: center; justify-content: flex-start;
    padding-top: 11px; color: var(--ink);
  }
  .treatment-item svg { width: 24px; height: 24px; }
  .treatment-label {
    margin-top: 6px; font-size: 9.5px; line-height: 1.1; text-align: center;
    text-transform: uppercase; font-weight: 400;
  }
  .divider { position: absolute; left: 60px; top: 276px; width: 185px; height: 8px; background: var(--white); }
  .claim-heading {
    position: absolute; left: 60px; top: 322px;
    font-weight: 500; font-size: 27px; line-height: 1.22; text-transform: uppercase;
  }
  .claim-copy {
    position: absolute; left: 60px; top: 455px; width: 360px;
    font-weight: 300; font-size: 14.5px; line-height: 1.42;
  }
  .claim-copy p + p { margin-top: 20px; }
  .accent-bar {
    position: absolute; left: 528px; top: 456px; width: 232px; height: 17px;
    background: linear-gradient(90deg, var(--navy), var(--green));
  }
  .room-photo { position: absolute; left: 455px; width: 305px; }
  .room-photo--bunks {
    top: 563px; height: 249px;
    background: linear-gradient(180deg, #e6e0d6 0%, var(--wall) 45%, #8a7462 75%, var(--wood-dark) 100%);
  }
  .room-photo--lounge {
    top: 822px; height: 256px;
    background: linear-gradient(180deg, #d9d0c2 0%, #b8aa98 40%, #5d5048 70%, var(--wood-dark) 100%);
  }
</style>
</head>
<body>
<main class="flyer">
  <div class="hero-lounge" role="img" aria-label="Photo of a lounge with a sofa and lamp, tinted blue to green"></div>
  <div class="hero-bedroom" role="img" aria-label="Photo of a bedroom with wooden bunk bed and wood floor"></div>
  <h1 class="hero-title">Residential/Inpatient<br>Recovery Center</h1>
  <div class="brand-badge"><span class="brand-name">Morval Care</span></div>

  <section class="info-panel">
    <h2 class="section-heading">What issues<br>can be treated?</h2>
    <ul class="treatment-list">
      <li class="treatment-item">
        <svg viewBox="0 0 24 24" fill="none" stroke="currentColor" stroke-width="1.4"><path d="M10 3h4v4l2 3v11H8V10l2-3z"/><path d="M8 13h8"/></svg>
        <span class="treatment-label">Alcoholism</span>
      </li>
      <li class="treatment-item">
        <svg viewBox="0 0 24 24" fill="none" stroke="currentColor" stroke-width="1.4"><path d="M17 3l4 4M19 5l-3 3M16 6l2 2-9 9-3 0 0-3z"/><path d="M6 17l-3 4"/></svg>
        <span class="treatment-label">Drug<br>addiction</span>
      </li>
      <li class="treatment-item">
        <svg viewBox="0 0 24 24" fill="none" stroke="currentColor" stroke-width="1.4"><rect x="2" y="8" width="10" height="6" rx="3" transform="rotate(-30 7 11)"/><circle cx="17" cy="14" r="4"/><path d="M14.5 16.5l5-5"/></svg>
        <span class="treatment-label">Medication<br>addiction</span>
      </li>
      <li class="treatment-item">
        <svg viewBox="0 0 24 24" fill="none" stroke="currentColor" stroke-width="1.4"><path d="M7 21v-4a7 7 0 1 1 10-6l1 3h-2v3h-3v4"/><circle cx="12" cy="10" r="2.5"/></svg>
        <span class="treatment-label">Behavioral<br>health</span>
      </li>
    </ul>
    <div class="divider"></div>
    <h2 class="claim-heading">Kentuckys leading<br>drug &amp; alcohol addiction<br>treatment</h2>
    <div class="claim-copy">
      <p>94% of those suffering from substance use disorder stay in active addiction without an intervention.</p>
      <p>We offer the most effective and comfortable treatment that leads to success.</p>
    </div>
  </section>

  <div class="accent-bar"></div>
  <div class="room-photo room-photo--bunks" role="img" aria-label="Photo of a shared room with bunk beds and a round table"></div>
  <div class="room-photo room-photo--lounge" role="img" aria-label="Photo of a room with bunk beds, chairs and a flower vase"></div>
</main>
</body>
</html>
```